Brenmoor Systems Website Revamp

We need a full website for the oil and gas sector to showcase our company and our technology/services we provide to larger corporations. We want our website represent innovation and identity.

Background:

We are a service based company that specializes in:

- well services, and
-permanent applications
**(Please be aware that these are two different aspects to the oil and gas sector, both of which we supply to our customers)

We provide a wide range of jet pump technologies to address under performing reservoirs or problematic well producing conditions. We have field operations currently in: Canada, Oman, and Australia with efforts currently underway to expand in other markets. Therefore are needing a website to help promote a better comprehension of what we do and how we can solve their well issues. We are looking for

1.) Identity;
2.) Emphasis on better comprehension of our services for our clients to relate to us as a solution to their needs;
3.) User friendly interface - but new and exciting in this digital age .

Some examples of websites we like:

http://quorvalinc.com/how-we-work/
http://www.tandrisystems.com/tandri-system/
https://mirelfield.com/

Videos of our technologies:

https://www.vidoquay.com/watch?v=Qm47TzxR2pa
https://www.vidoquay.com/watch?v=Lk8WnbeT5yc

Target Market(s)

Petroleum Industry Clients

Coding

Coded - Design and coding required

Number of Pages Required

5+ page

Colors

Designer to choose colors to be used in the design.

Requirements
Must have
• See Project Description, and feel free to contact us with any questions/inquiries!
Nice to have
• Our color scheme is generally 'blue', to depict jet pumps (our service). However, we are open to ideas and artistic interpretation. Grayscale/offset colors/highlight colors etc.

```html
<!DOCTYPE html>
<html lang="en">
<head>
<meta charset="utf-8">
<title>Brenmoor Systems</title>
<link rel="stylesheet" href="https://fonts.googleapis.com/css2?family=Michroma&family=Questrial&family=Montserrat:wght@400;600;700&display=swap">
<style>
:root{
  --accent:#2bb7ea;
  --accent-dark:#1a8fd8;
  --navy:#0b3f9e;
  --title-navy:#0d3e9c;
  --ink:#333;
  --muted:#666;
  --bar:#2f2f2f;
  --footer:#3b3b3b;
  --footer-low:#2c2c2c;
  --light:#f1f1f1;
  --white:#fff;
}
*{box-sizing:border-box;margin:0;padding:0}
html,body{width:1200px;height:3529px;overflow:hidden}
body{font-family:"Questrial",sans-serif;color:var(--ink);background:var(--white);position:relative}
a{color:inherit;text-decoration:none}
.section-title{font-family:"Michroma",sans-serif;font-size:24px;letter-spacing:1px;text-align:center;color:var(--title-navy);text-transform:uppercase}
.section-title span{color:var(--accent)}
.title-rule{width:110px;height:2px;background:#cfd7e2;margin:14px auto 0}
.btn{display:inline-block;font-family:"Questrial",sans-serif;border-radius:18px;font-size:14px;text-align:center}
.btn-dark{background:#3a3a3a;color:var(--white);padding:9px 28px}
.btn-blue{background:var(--accent);color:var(--white)}

/* top bar */
.top-bar{height:33px;background:var(--bar);display:flex;align-items:center;justify-content:space-between;padding:0 140px 0 146px;color:#ddd;font-size:12px}
.social{display:flex;gap:4px}
.social i{display:block;width:22px;height:22px;background:var(--accent)}
.social i+i{background:#4a4a4a}
.top-contact{display:flex;gap:26px;align-items:center}
.top-contact span{display:flex;align-items:center;gap:6px}
.top-contact .mail{text-decoration:underline}

/* header */
.site-header{height:66px;display:flex;align-items:center;padding:0 140px 0 142px;background:var(--white)}
.brand{display:flex;align-items:center;gap:10px;font-family:"Questrial",sans-serif;font-size:22px;color:var(--navy);width:300px}
.brand i{width:14px;height:14px;border-radius:50%;background:var(--accent)}
.division{font-size:10px;color:var(--navy);line-height:1.3;border-left:1px solid #ccc;padding-left:12px;margin-left:-30px}
.division b{display:block;font-size:13px}
.main-nav{margin-left:auto;display:flex;gap:36px;font-size:14px;color:#444}

/* hero */
.hero{height:449px;position:relative;background:linear-gradient(180deg,#5a6478 0%,#c97a3a 28%,#e8a050 36%,#6d6258 55%,#8c8a86 75%,#6f6e6c 100%);text-align:center;color:var(--white)}
.hero-title{position:absolute;top:140px;left:0;right:0;font-family:"Michroma",sans-serif;font-size:38px;line-height:1.45;letter-spacing:1px;text-transform:uppercase;text-shadow:0 2px 6px rgba(0,0,0,.4)}
.hero .btn-blue{position:absolute;top:272px;left:522px;width:156px;padding:9px 0;font-size:17px}
.dots{position:absolute;top:405px;left:0;right:0;display:flex;justify-content:center;gap:10px}
.dots i{width:8px;height:8px;border-radius:50%;background:#ddd}
.dots i:nth-child(3){background:var(--accent)}
.arrow{position:absolute;top:184px;width:40px;height:54px;display:flex;align-items:center;justify-content:center}
.arrow.prev{left:-14px;background:var(--white);border-radius:0 27px 27px 0}
.arrow.next{right:-14px;background:var(--accent);border-radius:27px 0 0 27px}

/* challenge */
.challenge{height:412px;padding-top:64px;text-align:center;background:linear-gradient(90deg,#fff 55%,#eef0f2 100%)}
.challenge .lead{width:760px;margin:36px auto 0;font-size:15px;line-height:1.6;color:#333}
.challenge .body{width:800px;margin:14px auto 0;font-size:12.5px;line-height:1.9;color:#444}
.challenge .btn{margin-top:30px}

/* apps */
.apps{height:424px;padding-top:48px;background:linear-gradient(90deg,#42c3f0 0%,#2ba4e6 100%);color:var(--white);text-align:center}
.apps .section-title{color:var(--white)}
.apps .title-rule{background:rgba(255,255,255,.5)}
.app-grid{display:flex;justify-content:center;gap:0;margin-top:58px}
.app{width:234px}
.app-icon{width:112px;height:112px;border-radius:50%;background:var(--white);border:5px solid rgba(255,255,255,.5);background-clip:padding-box;margin:0 auto;display:flex;align-items:center;justify-content:center}
.app h3{font-size:14px;margin-top:18px;font-weight:700;font-family:"Montserrat",sans-serif}
.app p{font-size:12px;line-height:1.6;margin:8px auto 0;width:180px;color:#e3f5ff}

/* solution */
.solution{height:510px;padding-top:68px;background:linear-gradient(90deg,#fff 55%,#eceef0 100%);position:relative}
.solution-body{position:absolute;top:134px;left:146px;display:flex}
.tabs{width:212px;border-right:2px solid #ddd;font-size:13px;color:#666;text-align:right}
.tabs li{list-style:none;padding:14px 16px 14px 0;border-bottom:1px solid #e2e2e2;line-height:1.3}
.tabs li.active{color:var(--accent);border-right:3px solid var(--accent);margin-right:-2px}
.solution-figure{width:246px;height:195px;margin-left:26px;background:linear-gradient(180deg,#e9eef3 0%,#cfd9e2 45%,#9a7a5c 60%,#7d644e 100%);border:1px solid #ccc}
.solution-text{width:474px;margin-left:26px;font-size:12.5px;line-height:1.9;color:#444}
.solution-text h4{font-family:"Michroma",sans-serif;font-size:13px;color:#333;font-weight:400;margin-bottom:6px}
.solution-text hr{border:0;border-top:1px solid #ccc;width:210px;margin-bottom:14px}
.solution-text p+p{margin-top:12px}
.solution .btn{position:absolute;top:1788px}

/* area */
.area{height:666px;background:var(--navy);color:var(--white);text-align:center;padding-top:54px;position:relative}
.area .section-title{color:var(--white)}
.area .title-rule{background:rgba(255,255,255,.4)}
.area p{font-size:14px;margin-top:16px}
.world-map{position:absolute;top:153px;left:100px;width:1000px;height:494px;background:linear-gradient(160deg,#5ecaf5 0%,#4cb8ee 50%,#3aa6e4 100%);border-radius:120px 180px 90px 140px;opacity:.85}
.pin{position:absolute}
.map-label{position:absolute;top:248px;left:226px;background:var(--white);color:#333;font-size:12px;padding:3px 16px;border-radius:10px}

/* contact */
.email{height:487px;text-align:center;padding-top:52px}
.email p{font-size:14px;margin-top:16px}
.contact-form{width:352px;margin:16px auto 0;text-align:left}
.field{height:31px;border:1px solid #e0e0e0;margin-bottom:10px;font-size:12px;color:#777;display:flex;align-items:center;gap:10px;padding-left:8px}
.field.message{height:116px;align-items:flex-start;padding-top:8px}
.email .btn-blue{display:block;width:104px;margin:26px auto 0;padding:7px 0;font-size:13px;font-weight:700;font-family:"Montserrat",sans-serif}

/* cta */
.cta{height:177px;background:var(--light);text-align:center;padding-top:52px}
.cta h2{font-family:"Montserrat",sans-serif;font-size:24px;font-weight:700;color:#222}
.cta h2 span{color:var(--accent)}
.cta .btn{margin-top:18px;padding:7px 26px;font-size:12px}

/* footer */
.site-footer{height:258px;background:var(--footer);color:#ddd;display:flex;padding:44px 0 0 142px;font-size:12px}
.footer-col h5{font-family:"Michroma",sans-serif;font-size:11px;font-weight:400;color:var(--white);padding-bottom:8px;border-bottom:1px solid #666;width:160px;margin-bottom:16px}
.quick-links{width:268px}
.quick-links li{list-style:none;margin-bottom:12px}
.contact-info{width:350px}
.info-row{display:flex;gap:12px;margin-bottom:16px;line-height:1.5}
.info-row i{width:18px;height:18px;background:var(--accent);border-radius:3px;flex:none}
.footer-brand{margin-top:40px;text-align:center}
.footer-brand .brand{color:var(--white);justify-content:center;width:auto}
.footer-brand .social{justify-content:center;margin-top:14px}
.copyright{height:47px;background:var(--footer-low);color:#ccc;font-size:12px;display:flex;align-items:center;justify-content:center}
</style>
</head>
<body>

<div class="top-bar">
  <div class="social"><i></i><i></i></div>
  <div class="top-contact">
    <span><svg width="12" height="12" viewBox="0 0 24 24"><path fill="#2bb7ea" d="M6.6 10.8a15 15 0 0 0 6.6 6.6l2.2-2.2c.3-.3.7-.4 1-.2 1.1.4 2.3.6 3.6.6.6 0 1 .4 1 1V20c0 .6-.4 1-1 1A17 17 0 0 1 3 4c0-.6.4-1 1-1h3.5c.6 0 1 .4 1 1 0 1.3.2 2.5.6 3.6.1.3 0 .7-.2 1z"/></svg>+1 (403) 555-0148</span>
    <span class="mail"><svg width="12" height="10" viewBox="0 0 24 18"><rect width="24" height="18" fill="#2bb7ea"/><path d="M0 0l12 9 12-9" stroke="#2f2f2f" fill="none"/></svg>info@brenmoorsystems.com</span>
  </div>
</div>

<header class="site-header">
  <div class="brand"><i></i>Brenmoor Systems</div>
  <div class="division">A Division of<b>Kellridge Stone</b>Energy Partners</div>
  <nav class="main-nav"><a>What We Do ⌄</a><a>Who We Are ⌄</a><a>Resources ⌄</a><a>Contact Us</a></nav>
</header>

<section class="hero" role="img" aria-label="Jet pump skid at a well site under a sunset sky">
  <h1 class="hero-title">We provide a wide range of<br>jet pump technologies.</h1>
  <a class="btn btn-blue">Contact Us</a>
  <div class="dots"><i></i><i></i><i></i><i></i></div>
  <span class="arrow prev"><svg width="12" height="18"><path d="M10 2L3 9l7 7" stroke="#333" stroke-width="2" fill="none"/></svg></span>
  <span class="arrow next"><svg width="12" height="18"><path d="M2 2l7 7-7 7" stroke="#fff" stroke-width="2" fill="none"/></svg></span>
</section>

<section class="challenge">
  <h2 class="section-title">The <span>Challenge</span></h2>
  <div class="title-rule"></div>
  <p class="lead">Lorem ipsum dolor sit amet, consectetuer adipiscing elit, sed diam nonummy nibh euismod tincidunt ut laoreet dolore magna aliquam erat volutpat.</p>
  <p class="body">Lorem Ipsum is simply dummy text of the printing and typesetting industry. Lorem Ipsum has been the industry's standard dummy text ever since the 1500s, when an unknown printer took a galley of type and scrambled it to make a type specimen book. It has survived not only five centuries, but also the leap into electronic typesetting, remaining essentially unchanged. It was popularised in the 1960s with the release of Letraset sheets containing Lorem Ipsum passages, and more recently with desktop.</p>
  <a class="btn btn-dark">Learn More</a>
</section>

<section class="apps">
  <h2 class="section-title">The Apps</h2>
  <div class="title-rule"></div>
  <div class="app-grid">
    <div class="app">
      <div class="app-icon"><svg width="46" height="46" viewBox="0 0 46 46" fill="none" stroke="#444" stroke-width="3"><rect x="8" y="6" width="14" height="30"/><path d="M22 12h12v8M28 20h12M15 36v6M6 42h34"/></svg></div>
      <h3>Permanent Artificial Lift</h3>
      <p>It is a long established fact that a reader will be distracted by the readable content of a page when looking at its layout.</p>
    </div>
    <div class="app">
      <div class="app-icon"><svg width="46" height="46" viewBox="0 0 46 46"><circle cx="18" cy="24" r="10" fill="none" stroke="#444" stroke-width="6" stroke-dasharray="4 3"/><circle cx="18" cy="24" r="4" fill="#444"/><circle cx="34" cy="12" r="6" fill="none" stroke="#444" stroke-width="4" stroke-dasharray="3 2"/></svg></div>
      <h3>Well Services</h3>
      <p>It is a long established fact that a reader will be distracted by the readable content of a page when looking at its layout.</p>
    </div>
    <div class="app">
      <div class="app-icon"><svg width="46" height="46" viewBox="0 0 46 46" fill="none" stroke="#444" stroke-width="3"><circle cx="34" cy="12" r="6"/><circle cx="10" cy="36" r="4"/><path d="M14 34c10-2 2-12 14-18"/></svg></div>
      <h3>Locations</h3>
      <p>It is a long established fact that a reader will be distracted by the readable content of a page when looking at its layout.</p>
    </div>
    <div class="app">
      <div class="app-icon"><svg width="46" height="46" viewBox="0 0 46 46"><circle cx="23" cy="23" r="19" fill="none" stroke="#444" stroke-width="3"/><path fill="#444" d="M16 18c2 6 6 10 12 12l3-3 4 3-2 4c-9-1-17-9-18-18l4-2 3 4z"/></svg></div>
      <h3>Contact Us</h3>
      <p>It is a long established fact that a reader will be distracted by the readable content of a page when looking at its layout.</p>
    </div>
  </div>
</section>

<section class="solution">
  <h2 class="section-title">The <span>Solution</span></h2>
  <div class="title-rule"></div>
  <div class="solution-body">
    <ul class="tabs">
      <li class="active">Horizontal &amp; Deviated Wells</li>
      <li>Rig-less Pump Changes</li>
      <li>Low HP Requirement Surface</li>
      <li>Pad Well Systems</li>
      <li>Sand Handling Capabilities</li>
      <li>Gas Handling Capabilities</li>
    </ul>
    <div class="solution-figure" role="img" aria-label="Cross-section diagram of a horizontal well with a jet pump placed along the lateral"></div>
    <div class="solution-text">
      <h4>Horizontal &amp; Deviated Wells</h4>
      <hr>
      <p>With no moving parts, the KSEP jet pump takes the industry to the next level, allowing for jet pump placement anywhere in the horizontal profile. Using power fluid as the drive mechanism of a jet pump, the system has no problems with deviated, crooked or horizontal wellbores.</p>
      <p>With a jet pump landed in the horizontal section of a well, operators are not only able to achieve higher inflow rates, they are also able to achieve higher ultimate reserve recovery.</p>
    </div>
  </div>
  <a class="btn btn-dark" style="position:absolute;top:404px;left:384px">Learn More</a>
</section>

<section class="area">
  <h2 class="section-title">Area of Operations</h2>
  <div class="title-rule"></div>
  <p>We have field operations currently in: Canada, Oman, and Australia</p>
  <div class="world-map" role="img" aria-label="World map highlighting Canada, Oman and Australia"></div>
  <span class="map-label">Canada</span>
  <svg class="pin" style="top:210px;left:320px" width="40" height="52" viewBox="0 0 40 52"><path d="M20 50C8 32 2 26 2 18a18 18 0 0 1 36 0c0 8-6 14-18 32z" fill="#fff"/><circle cx="20" cy="18" r="10" fill="#e53935"/></svg>
  <svg class="pin" style="top:300px;left:678px" width="40" height="52" viewBox="0 0 40 52"><path d="M20 50C8 32 2 26 2 18a18 18 0 0 1 36 0c0 8-6 14-18 32z" fill="#555"/><circle cx="20" cy="18" r="10" fill="#e53935"/></svg>
  <svg class="pin" style="top:452px;left:922px" width="40" height="52" viewBox="0 0 40 52"><path d="M20 50C8 32 2 26 2 18a18 18 0 0 1 36 0c0 8-6 14-18 32z" fill="#555"/><circle cx="20" cy="18" r="10" fill="#1e5fb8"/></svg>
</section>

<section class="email">
  <h2 class="section-title">Send Us <span>An Email</span></h2>
  <div class="title-rule"></div>
  <p>Lorem ipsum dolor sit amet.</p>
  <form class="contact-form">
    <div class="field"><svg width="12" height="12" viewBox="0 0 24 24"><circle cx="12" cy="7" r="5" fill="#666"/><path d="M2 24c0-6 4-9 10-9s10 3 10 9z" fill="#666"/></svg>Name*</div>
    <div class="field"><svg width="12" height="12" viewBox="0 0 24 24"><path fill="#666" d="M6.6 10.8a15 15 0 0 0 6.6 6.6l2.2-2.2c.3-.3.7-.4 1-.2 1.1.4 2.3.6 3.6.6.6 0 1 .4 1 1V20c0 .6-.4 1-1 1A17 17 0 0 1 3 4c0-.6.4-1 1-1h3.5c.6 0 1 .4 1 1 0 1.3.2 2.5.6 3.6.1.3 0 .7-.2 1z"/></svg>Phone*</div>
    <div class="field"><svg width="12" height="10" viewBox="0 0 24 18"><rect width="24" height="18" fill="#666"/><path d="M0 0l12 9 12-9" stroke="#fff" fill="none"/></svg>Email*</div>
    <div class="field message"><svg width="12" height="12" viewBox="0 0 24 24"><circle cx="12" cy="12" r="10" fill="#666"/></svg>Message</div>
  </form>
  <a class="btn btn-blue">SUBMIT</a>
</section>

<section class="cta">
  <h2>FIND OUT HOW THE <span>BRENMOOR SYSTEMS</span> CAN WORK FOR YOU.</h2>
  <a class="btn btn-dark">CONTACT US</a>
</section>

<footer class="site-footer">
  <div class="footer-col quick-links">
    <h5>QUICK LINKS</h5>
    <ul><li>› What We Do ⌄</li><li>› Who We Are ⌄</li><li>› Resources ⌄</li><li>› Contact Us ⌄</li></ul>
  </div>
  <div class="footer-col contact-info">
    <h5>CONTACT INFO</h5>
    <div class="info-row"><i></i><div><b>Brenmoor Systems</b><br>Lorem Ipsum is simply dummy text<br>of the printing and type settin...</div></div>
    <div class="info-row"><i></i><div>+1 403.555.0148</div></div>
    <div class="info-row"><i></i><div>office@brenmoorsystems.com</div></div>
  </div>
  <div class="footer-brand">
    <div class="brand"><i></i>Brenmoor Systems</div>
    <div class="social"><i></i><i></i></div>
  </div>
</footer>
<div class="copyright">© Copyright 2018 - Brenmoor Systems. All Rights Reserved.</div>

</body>
</html>
```